Business Cards Needed for Innovative Healthcare Marketing Company

We are a marketing company focused on healthcare. Our company is all about rebranding yourself renewing your image and generating results. The phoenix stands for "reborn" or "rising" which we provide new brands for our clients we take their old brands and renew it with creativity and innovation. I am looking for a business card with color dimension. I have attached an example of a card I think has the look and feel of what I am trying to accomplish. I like that the card example has black and grey font colors, I like the font placement and the small logo, I really like the use of the colors on the right those are the colors of my logo. My logo is phoenix so maybe incorporating flames similar to that design. I would like the back a solid color maybe red with an opaque version of the logo and website. As a marketing company I am always open to creative liberty!

Target Market(s)

Doctors and business professionals.

Industry/Entity Type

Marketing

Contact Information for Business Card

Vornaly Health Care Marketing
Marnie Okonski- CEO
#(502)638-2947
email-marnie@vornaly.com
website- vornaly.com

Font styles to use
Sans Serif

Colors
ec1f27
f37122
ffc214
fbed22
fbf289
f04a50

Requirements
Must have
• The logo and required information
Nice to have
• icons by the information
Should not have
• child like font

```html
<!DOCTYPE html>
<html lang="en">
<head>
<meta charset="utf-8">
<title>Vornaly Health Care Marketing – Business Cards</title>
<link rel="stylesheet" href="https://fonts.googleapis.com/css2?family=Raleway:wght@300;400&family=Open+Sans:wght@400;700&display=swap">
<style>
  :root {
    --page: #232323;
    --card: #ffffff;
    --brand-red: #b3262e;
    --deep-red: #a8202a;
    --flame-orange: #f37122;
    --amber: #f0a23a;
    --gold: #ffc214;
    --ink-grey: #5a5a5a;
    --soft-grey: #6e6e6e;
  }
  * { box-sizing: border-box; margin: 0; padding: 0; }
  html, body { width: 1200px; height: 950px; overflow: hidden; }
  body {
    background: var(--page);
    display: flex;
    flex-direction: column;
    align-items: center;
    justify-content: center;
    gap: 50px;
    font-family: "Open Sans", Arial, sans-serif;
  }
  .card {
    position: relative;
    width: 700px;
    height: 400px;
    background: var(--card);
    overflow: hidden;
  }

  /* Back of card */
  .card--back {
    display: flex;
    flex-direction: column;
    align-items: center;
    justify-content: center;
  }
  .back-brand {
    display: flex;
    align-items: center;
    gap: 22px;
  }
  .brand-dot {
    width: 64px;
    height: 64px;
    border-radius: 50%;
    background: var(--flame-orange);
  }
  .brand-name {
    font-family: "Raleway", Arial, sans-serif;
    font-weight: 300;
    color: var(--brand-red);
    letter-spacing: 2px;
    line-height: 1.1;
  }
  .brand-name .line-main { display: block; font-size: 46px; }
  .brand-name .line-sub { display: block; font-size: 15px; letter-spacing: 3px; margin-top: 6px; }
  .back-web {
    margin-top: 52px;
    font-size: 15px;
    letter-spacing: 6px;
    color: var(--ink-grey);
  }

  /* Front of card */
  .front-art {
    position: absolute;
    right: 0;
    top: 0;
    width: 420px;
    height: 400px;
  }
  .front-brand {
    position: absolute;
    left: 56px;
    top: 92px;
  }
  .front-brand .line-main { font-size: 44px; }
  .front-brand .line-sub { font-size: 14px; }
  .person {
    position: absolute;
    left: 56px;
    top: 236px;
  }
  .person-name {
    font-weight: 700;
    font-size: 22px;
    color: var(--deep-red);
  }
  .person-role {
    font-weight: 700;
    font-size: 15px;
    color: var(--amber);
    margin: 4px 0 10px 20px;
  }
  .contact-list { list-style: none; margin-left: 20px; }
  .contact-item {
    display: flex;
    align-items: center;
    gap: 10px;
    font-size: 16px;
    color: var(--soft-grey);
    line-height: 27px;
  }
  .contact-icon { width: 16px; height: 16px; flex: none; }
</style>
</head>
<body>

  <section class="card card--back">
    <div class="back-brand">
      <span class="brand-dot"></span>
      <p class="brand-name"><span class="line-main">VORNALY</span><span class="line-sub">HEALTH CARE MARKETING</span></p>
    </div>
    <p class="back-web">www.vornaly.com</p>
  </section>

  <section class="card card--front">
    <svg class="front-art" viewBox="0 0 420 400" role="img" aria-label="Large rising phoenix illustration in red to orange gradient">
      <defs>
        <linearGradient id="flame" x1="0" y1="0" x2="0.6" y2="1">
          <stop offset="0" stop-color="#a8202a"/>
          <stop offset="0.55" stop-color="#d8582a"/>
          <stop offset="1" stop-color="#f0a23a"/>
        </linearGradient>
      </defs>
      <path d="M40 120 C40 40 150 0 250 0 L420 0 L420 230 C420 320 330 380 250 400 L200 400 C130 330 40 230 40 120 Z" fill="url(#flame)"/>
    </svg>

    <p class="brand-name front-brand"><span class="line-main">VORNALY</span><span class="line-sub">HEALTH CARE MARKETING</span></p>

    <div class="person">
      <p class="person-name">Marnie Okonski</p>
      <p class="person-role">CEO</p>
      <ul class="contact-list">
        <li class="contact-item">
          <svg class="contact-icon" viewBox="0 0 16 16" aria-hidden="true"><path fill="#b3262e" d="M1 5 C1 2 15 2 15 5 L12 6 L11 4.5 H5 L4 6 Z M4 7 H12 L14 14 H2 Z"/><circle cx="8" cy="10.5" r="2" fill="#fff"/></svg>
          <span>(502)638-2947</span>
        </li>
        <li class="contact-item">
          <svg class="contact-icon" viewBox="0 0 16 16" aria-hidden="true"><rect x="1" y="3" width="14" height="10" rx="1" fill="#b3262e"/><path d="M1.5 4 L8 9 L14.5 4" stroke="#fff" stroke-width="1.3" fill="none"/></svg>
          <span>marnie@vornaly.com</span>
        </li>
        <li class="contact-item">
          <svg class="contact-icon" viewBox="0 0 16 16" aria-hidden="true"><circle cx="8" cy="8" r="7" fill="#b3262e"/><path d="M1 8 H15 M8 1 C4 5 4 11 8 15 M8 1 C12 5 12 11 8 15" stroke="#fff" stroke-width="1" fill="none"/></svg>
          <span>www.vornaly.com</span>
        </li>
      </ul>
    </div>
  </section>

</body>
</html>
```